Label for luxury drink/cocktail flavour bags

I need a luxury label designed for our new product, which are infusion bags for drinks and cocktails. We are a saffron producer so all will contain saffron and the name of the product is Velvet Draughts. There will be 10 bags in each pack, and the packaging will be a cardboard cylinder which is 105mm high x 85mm wide. The tagline is "Elevate every pour", and the first variety will be called Gilded Blush. The ingredients are saffron, rose petals and hibiscus flower. The label needs to feel luxurious, and I would like a gold foil element in the final printing so please include that in the design. Our brand is Wexmoor Australian Saffron. I like clean designs, without excessive detail but would be open to some saffron flower illustrations included. The design needs to be editable for different blends as we release them.

Target Market(s)

30-60 year old females with a high income

Industry/Entity Type

Food and drink

Requirements
Must have
• Elevate every pour, Brand, Ingredients section (for this one, Saffron, Rose Petals, Hibiscus Flowers), and one of the attached "made in" marks on the pack

```html
<!DOCTYPE html>
<html lang="en">
<head>
<meta charset="utf-8">
<title>Velvet Draughts – Gilded Blush Label</title>
<link rel="stylesheet" href="https://fonts.googleapis.com/css2?family=Montserrat:wght@500;600;700&display=swap">
<style>
  :root {
    --page: #ffffff;
    --ink: #111111;
    --frame: #1a1a1a;
    --flower-light: #f4f3f3;
    --flower-mid: #e7e5e5;
    --badge-green: #00875a;
    --gold-dark: #a8802f;
    --gold-mid: #d4b062;
    --gold-light: #f3e1a4;
  }
  * { margin: 0; padding: 0; box-sizing: border-box; }
  html, body {
    width: 1200px; height: 1200px; overflow: hidden;
    background: var(--page);
    font-family: "Montserrat", sans-serif;
    color: var(--ink);
  }
  .canvas { position: relative; width: 1200px; height: 1200px; }
  .label {
    position: absolute; left: 214px; top: 301px;
    width: 747px; height: 604px;
    border: 1.5px solid var(--frame);
    overflow: hidden;
  }
  .flower-art {
    position: absolute; left: 72px; top: 168px;
    width: 305px; height: 440px;
    background: radial-gradient(ellipse at 55% 35%, var(--flower-mid) 0%, var(--flower-light) 55%, rgba(255,255,255,0) 78%);
    border-radius: 45% 45% 10% 10%;
  }
  .brand {
    position: absolute; left: 98px; top: 50px; width: 290px;
    text-align: center; font-weight: 700; color: var(--ink);
  }
  .brand-name { font-size: 26px; letter-spacing: 0.58em; padding-left: 0.58em; line-height: 1; }
  .brand-sub { font-size: 9.5px; letter-spacing: 0.62em; padding-left: 0.62em; margin-top: 14px; }
  .product-name {
    position: absolute; left: 0; top: 174px; width: 486px;
    text-align: center; font-weight: 600;
    font-size: 48px; line-height: 45px; letter-spacing: 0.1em; padding-left: 0.1em;
  }
  .variety, .count {
    position: absolute; left: 0; width: 486px;
    text-align: center; font-weight: 500;
    font-size: 28px; letter-spacing: 0.2em; padding-left: 0.2em;
  }
  .variety { top: 392px; color: var(--gold-dark); font-weight: 600; }
  .count { top: 540px; }
  .info {
    position: absolute; left: 477px; top: 110px; width: 230px;
    text-align: center; font-weight: 500;
  }
  .info-title { font-size: 23px; line-height: 28px; font-weight: 500; }
  .info-list { font-size: 14.5px; line-height: 18px; margin-top: 18px; }
  .foil-rule {
    width: 75px; height: 3px; margin: 70px auto 0;
    background: linear-gradient(90deg, var(--gold-dark), var(--gold-light) 50%, var(--gold-mid));
  }
  .tagline { font-size: 18px; line-height: 24px; margin-top: 34px; letter-spacing: 0.04em; }
  .origin-badge { position: absolute; left: 507px; top: 445px; }
</style>
</head>
<body>
<div class="canvas">
  <div class="label">
    <div class="flower-art" role="img" aria-label="Faint grey line illustration of saffron crocus flowers with long leaves"></div>

    <div class="brand">
      <div class="brand-name">WEXMOOR</div>
      <div class="brand-sub">AUSTRALIAN SAFFRON</div>
    </div>

    <h1 class="product-name">VELVET<br>DRAUGHTS</h1>
    <div class="variety">GILDED BLUSH</div>
    <div class="count">10 BAGS</div>

    <div class="info">
      <h2 class="info-title">Ingredients</h2>
      <p class="info-list">Saffron, Rose Petals,<br>Hibiscus Flowers</p>
      <div class="foil-rule"></div>
      <p class="tagline">Elevate<br>every pour</p>
    </div>

    <svg class="origin-badge" width="170" height="46" viewBox="0 0 170 46" role="img" aria-label="Country of origin mark">
      <rect x="1" y="1" width="168" height="44" rx="4" fill="none" stroke="var(--badge-green)" stroke-width="2"/>
    </svg>
  </div>
</div>
</body>
</html>
```